We need a book cover for a novel called "Nine Lanterns".

In essence it is a novel about a girl, Mina Corbett, who owns an Antique Shop, The Brass Thimble Parlour, in modern day London. She buys the contents of the deceased estate of Margaret Dunmore. Amongst that estate is a box of old English postcards, each postcard providing a snippet of life in London during WWII, all signed by the mysterious "B", and all addressed to "Phil". Whilst Mina is cleaning and pricing some of the belongings from that estate she is unexpectedly transported back in time. She ends up in New Zealand in 1860 at the time of the gold rush; in India in 1856, just as the Indian Revolt occurs; in London in 1896 staying at the Halvern hotel, and again in London during the Blitz.
This is the Relic Hunters' Tour woven into the pages of a book as you follow the journey of silver, rubies and diamonds, greenstone and tiger knives (Katar). A novel where tiger hunts and ruby necklaces are entwined with murders and maids.
Each story forms part of the story of Margaret Dunmore and the history of her family.
The different stories are magically woven together into a climatic ending, involving auction houses, deadly collectors, and love.

Below is the blurb for the back cover:

"Following the unexplained disappearance of her parents, and in a last ditch attempt to save the antique store she has inherited from financial ruin, Mina Corbett takes on a deceased estate. Amongst the estate is a collection of fifteen vintage postcards.

Mina is unprepared for the enigma these postcards hint at about their reclusive former owner. They consume her and complicate her life in unimaginable ways.

A novel traversing three continents, and two centuries, where tiger hunts and ruby necklaces are irrevocably entwined with murders and mysteries, auction houses and antiquities.

It might also explain what happened to her parents ..."

This is the Pinterest board with some images on it which capture the essence of the book. http://www.pinboardly.example/tuimrsfox/possible-book-cover-inspirations/

The authors name is Rowena Talbridge. Below is the blurb about the author to be included on the back cover:

"Rowena Talbridge has worked in her family's antique store since she was a toddler.
She’s gone from being allowed to sell 50c postcards in the corner of Relic Row, a literal treasure trove, to selling $5,000 Brandholt vases at prestigious antique fairs around New Zealand.
She lives in Auckland with her husband and two daughters."

Just added the "blurb" for the back of the book to the brief. Thank you.

Added the Author Blurb to the design brief and a few more images of stamps & postmarks for reference.

Just amended the blurb. Thanks. Last change.

Just updated the blurb and the author's blurb for the back cover in the brief. Please use this latest version. Also loaded an image of the author for the back cover. Please incorporate this in your design for the back cover (not too large though). Thank you so very much.

Target Market(s)

The target reader is a woman, but ideally the cover shouldn't be too feminine.

Font styles to use
Script

Requirements
Must have
• Author's name at the bottom, centre. In a plain font.
Nice to have
• A postmark or a stamp or an old postcard/letter image somewhere.
Should not have
• No feather quills.

```html
<!DOCTYPE html>
<html lang="en">
<head>
<meta charset="utf-8">
<title>Nine Lanterns — Cover Wrap</title>
<link rel="stylesheet" href="https://fonts.googleapis.com/css2?family=Kaushan+Script&family=IM+Fell+English&family=Crimson+Text:wght@400&display=swap">
<style>
  :root {
    --stage: #3f3a37;
    --stage-light: #575050;
    --cover-mauve: #8c7480;
    --cover-dusk: #5f4a56;
    --cover-shadow: #4a3842;
    --back-dark: #2b1b1e;
    --back-deep: #1e1214;
    --ink-cream: #f2ede6;
    --ink-soft: #ddd3cc;
    --blade-silver: #d9d6d2;
    --blade-bright: #eeebe7;
    --blade-shadow: #a8a29e;
    --frame-white: #f7f5f2;
    --isbn-white: #f4f4f2;
    --isbn-ink: #2a2a2a;
  }
  * { margin: 0; padding: 0; box-sizing: border-box; }
  html, body { width: 1200px; height: 800px; overflow: hidden; }
  body {
    background: radial-gradient(ellipse at 50% 40%, var(--stage-light), var(--stage) 75%);
    position: relative;
  }
  .cover-wrap {
    position: absolute;
    left: 143px;
    top: 80px;
    width: 914px;
    height: 640px;
    display: flex;
    box-shadow: 0 18px 40px rgba(0,0,0,0.45);
  }

  /* Back cover */
  .back-cover {
    position: relative;
    width: 427px;
    height: 100%;
    background: linear-gradient(160deg, var(--cover-dusk), var(--cover-shadow) 55%, var(--back-dark));
    display: flex;
  }
  .author-column {
    width: 205px;
    height: 100%;
    background: linear-gradient(180deg, var(--back-deep), var(--back-dark) 60%, #3a2529);
    padding: 26px 18px 22px;
    display: flex;
    flex-direction: column;
    color: var(--ink-cream);
  }
  .author-photo-frame {
    width: 150px;
    height: 122px;
    background: var(--frame-white);
    padding: 7px;
    margin: 0 auto 14px;
    transform: rotate(-1.5deg);
    box-shadow: 0 3px 8px rgba(0,0,0,0.5);
  }
  .author-photo {
    width: 100%;
    height: 100%;
    background: linear-gradient(135deg, #3c6a2c, #6e9a3e 55%, #2d4a22);
  }
  .author-name {
    font-family: "IM Fell English", serif;
    font-size: 19px;
    font-weight: 400;
    line-height: 1.1;
  }
  .author-label {
    font-family: "Crimson Text", serif;
    font-size: 13px;
    margin-bottom: 12px;
    color: var(--ink-soft);
  }
  .author-bio p {
    font-family: "Crimson Text", serif;
    font-size: 10.5px;
    line-height: 1.45;
    margin-bottom: 9px;
    color: var(--ink-soft);
  }
  .back-title {
    margin-top: auto;
    font-family: "Kaushan Script", cursive;
    font-size: 30px;
    line-height: 0.95;
    color: var(--ink-cream);
    transform: rotate(-4deg);
    margin-left: 8px;
  }
  .back-title span { display: block; }
  .back-title span + span { padding-left: 18px; }
  .site-address {
    font-family: "Crimson Text", serif;
    font-size: 11px;
    color: var(--ink-soft);
    margin-top: 10px;
    text-align: center;
  }
  .blurb {
    width: 222px;
    padding: 26px 14px 0 16px;
    color: var(--ink-cream);
  }
  .blurb p {
    font-family: "Crimson Text", serif;
    font-size: 11px;
    line-height: 1.5;
    margin-bottom: 12px;
  }

  /* Spine */
  .spine {
    position: relative;
    width: 60px;
    height: 100%;
    background: linear-gradient(90deg, var(--cover-shadow), var(--cover-dusk) 50%, var(--cover-shadow));
    display: flex;
    flex-direction: column;
    align-items: center;
    padding-top: 22px;
    border-left: 1px solid rgba(0,0,0,0.25);
    border-right: 1px solid rgba(0,0,0,0.25);
  }
  .spine-title {
    writing-mode: vertical-rl;
    font-family: "Kaushan Script", cursive;
    font-size: 26px;
    color: var(--ink-cream);
    line-height: 1;
  }
  .spine-emblem {
    width: 36px;
    height: 44px;
    margin: 24px 0 20px;
    border-radius: 6px;
    background: radial-gradient(ellipse at 50% 50%, var(--blade-bright), var(--blade-silver) 45%, rgba(168,162,158,0) 100%);
  }
  .spine-author {
    writing-mode: vertical-rl;
    font-family: "IM Fell English", serif;
    font-size: 17px;
    color: var(--ink-cream);
  }
  .isbn-box {
    position: absolute;
    bottom: 36px;
    left: 4px;
    width: 52px;
    height: 120px;
    background: var(--isbn-white);
    display: flex;
    align-items: flex-start;
    justify-content: center;
    padding-top: 10px;
  }
  .isbn-label {
    writing-mode: vertical-rl;
    font-family: "Crimson Text", serif;
    font-size: 15px;
    letter-spacing: 1px;
    color: var(--isbn-ink);
  }

  /* Front cover */
  .front-cover {
    position: relative;
    width: 427px;
    height: 100%;
    background:
      radial-gradient(ellipse at 60% 55%, rgba(255,255,255,0.10), transparent 60%),
      linear-gradient(165deg, var(--cover-mauve), var(--cover-dusk) 70%, var(--cover-shadow));
    overflow: hidden;
  }
  .front-crack {
    position: absolute;
    inset: 0;
    width: 100%;
    height: 100%;
  }
  .front-title {
    position: absolute;
    top: 34px;
    left: 40px;
    font-family: "Kaushan Script", cursive;
    font-weight: 400;
    color: var(--ink-cream);
    font-size: 62px;
    line-height: 0.92;
    transform: rotate(-4deg);
  }
  .front-title span { display: block; }
  .front-title span + span { padding-left: 46px; }
  .katar-art {
    position: absolute;
    left: 70px;
    top: 200px;
    width: 300px;
    height: 210px;
    border-radius: 18px;
    background: radial-gradient(ellipse at 55% 50%, rgba(238,235,231,0.85), rgba(217,214,210,0.55) 40%, rgba(168,162,158,0.18) 70%, rgba(168,162,158,0) 100%);
  }
  .front-author {
    position: absolute;
    bottom: 52px;
    left: 0;
    width: 100%;
    text-align: center;
    font-family: "IM Fell English", serif;
    font-size: 34px;
    color: var(--ink-cream);
    letter-spacing: 0.5px;
  }
</style>
</head>
<body>
  <main class="cover-wrap">
    <section class="back-cover">
      <aside class="author-column">
        <div class="author-photo-frame">
          <div class="author-photo" role="img" aria-label="Photograph of the author reading a book outdoors among green foliage"></div>
        </div>
        <h2 class="author-name">Rowena Talbridge</h2>
        <p class="author-label">about the author</p>
        <div class="author-bio">
          <p>Rowena Talbridge has worked in her family’s antique store since she was a toddler.</p>
          <p>She’s gone from being allowed to sell 50c postcards in the corner of Relic Row, a literal treasure trove, to selling $5,000 Brandholt vases at prestigious antique fairs around New Zealand.</p>
          <p>She lives in Auckland with her husband and two daughters.</p>
          <p>This is her first novel.</p>
        </div>
        <p class="back-title"><span>Nine</span><span>Lanterns</span></p>
        <p class="site-address">www.ninelanterns.example</p>
      </aside>
      <div class="blurb">
        <p>Following the unexplained disappearance of her parents, and in a last ditch attempt to save the antique store she has inherited from financial ruin, Mina Corbett takes on a deceased estate. Amongst the estate is a collection of fifteen vintage postcards.</p>
        <p>Mina is unprepared for the enigma these postcards hint at about their reclusive former owner. They consume her and complicate her life in unimaginable ways.</p>
        <p>A novel traversing three continents, and two centuries, where tiger hunts and ruby necklaces are irrevocably entwined with murders and mysteries, auction houses and antiquities.</p>
        <p>It might also explain what happened to her parents ...</p>
      </div>
    </section>

    <section class="spine">
      <p class="spine-title">Nine Lanterns</p>
      <div class="spine-emblem" role="img" aria-label="Small silver katar dagger folded like a paper plane"></div>
      <p class="spine-author">Rowena Talbridge</p>
      <div class="isbn-box"><span class="isbn-label">ISBN</span></div>
    </section>

    <section class="front-cover">
      <svg class="front-crack" viewBox="0 0 427 640" aria-hidden="true">
        <path d="M0 330 C80 320 140 350 210 335 S340 300 427 318" fill="none" stroke="rgba(40,25,35,0.35)" stroke-width="2"/>
        <path d="M250 640 C260 560 240 500 270 440" fill="none" stroke="rgba(40,25,35,0.25)" stroke-width="1.5"/>
      </svg>
      <h1 class="front-title"><span>Nine</span><span>Lanterns</span></h1>
      <div class="katar-art" role="img" aria-label="Illustration of a silver katar dagger with red ruby settings, folded like a paper plane, resting on cracked plaster"></div>
      <p class="front-author">Rowena Talbridge</p>
    </section>
  </main>
</body>
</html>
```